Tarvimoor business cards

Need fresh design for our business cards. Logo must be specific, we are open for everything else.

Contact Information for Business Card

phrase "GMP & JANITORIAL SERVICES" should be used as main point of card

Colors
3176b5
3276b5
85acd3
cedeed
ffffff
0292cd
33a6d7
85cae6
cee9f5

Requirements
Must have
• The logo
Should not have
• crowded designs

```html
<!DOCTYPE html>
<html lang="en">
<head>
<meta charset="utf-8">
<title>Tarvimoor Business Cards</title>
<link rel="stylesheet" href="https://fonts.googleapis.com/css2?family=Open+Sans:wght@400;600;700&display=swap">
<style>
  :root {
    --brand-blue: #0080c0;
    --text-grey: #4a4a4a;
    --divider-grey: #c4c4c4;
    --card-white: #ffffff;
    --backdrop: #ece9e4;
    --card-shadow: rgba(0, 0, 0, 0.28);
  }
  * { box-sizing: border-box; margin: 0; padding: 0; }
  html, body {
    width: 1200px;
    height: 1040px;
    overflow: hidden;
  }
  body {
    position: relative;
    background: var(--backdrop);
    font-family: "Open Sans", Arial, sans-serif;
  }
  .card {
    position: absolute;
    left: 285px;
    width: 640px;
    height: 366px;
    box-shadow: 2px 3px 4px var(--card-shadow);
  }
  .card--front { top: 130px; background: var(--card-white); }
  .card--back { top: 567px; background: var(--brand-blue); }

  .brand {
    position: absolute;
    display: flex;
    flex-direction: column;
    align-items: flex-end;
    white-space: nowrap;
  }
  .wordmark {
    font-family: "Open Sans", Arial, sans-serif;
    font-weight: 400;
    display: flex;
    align-items: center;
    line-height: 1;
  }
  .wordmark__dot {
    display: inline-block;
    border-radius: 50%;
  }
  .brand__tagline {
    font-family: "Open Sans", Arial, sans-serif;
    font-weight: 600;
    line-height: 1;
  }

  .card--front .brand {
    left: 78px;
    width: 252px;
    top: 166px;
    color: var(--brand-blue);
  }
  .card--front .wordmark {
    font-size: 33px;
    letter-spacing: 3.5px;
    margin-right: -3.5px;
  }
  .card--front .wordmark__dot {
    width: 11px; height: 11px;
    background: var(--brand-blue);
    margin-right: 12px;
  }
  .card--front .brand__tagline {
    margin-top: 6px;
    font-size: 8px;
    letter-spacing: 1.9px;
    margin-right: -1.9px;
  }

  .card--back .brand {
    left: 0; right: 0;
    top: 158px;
    align-items: center;
    color: var(--card-white);
  }
  .card--back .brand__inner {
    display: flex;
    flex-direction: column;
    align-items: flex-end;
  }
  .card--back .wordmark {
    font-size: 50px;
    letter-spacing: 6px;
    margin-right: -6px;
  }
  .card--back .wordmark__dot {
    width: 16px; height: 16px;
    background: var(--card-white);
    margin-right: 18px;
  }
  .card--back .brand__tagline {
    margin-top: 8px;
    font-size: 11px;
    letter-spacing: 2.8px;
    margin-right: -2.8px;
  }

  .divider {
    position: absolute;
    left: 350px;
    top: 70px;
    width: 2px;
    height: 230px;
    background: linear-gradient(to bottom, rgba(196,196,196,0), var(--divider-grey) 15%, var(--divider-grey) 85%, rgba(196,196,196,0));
  }
  .contact {
    position: absolute;
    left: 377px;
    top: 78px;
    color: var(--text-grey);
  }
  .contact__name {
    font-size: 23px;
    font-weight: 700;
    color: var(--brand-blue);
    line-height: 1.2;
  }
  .contact__role {
    font-size: 16.5px;
    line-height: 1.2;
    margin-bottom: 6px;
  }
  .contact__address {
    font-size: 16px;
    line-height: 20px;
    margin-bottom: 8px;
  }
  .contact__list { list-style: none; }
  .contact__item {
    display: flex;
    align-items: center;
    font-size: 16px;
    line-height: 21px;
  }
  .contact__icon {
    width: 14px;
    height: 14px;
    margin-right: 13px;
    fill: var(--brand-blue);
    flex: none;
  }

  .website {
    position: absolute;
    left: 0; right: 0;
    top: 296px;
    text-align: center;
    color: var(--card-white);
    font-size: 17px;
    letter-spacing: 12px;
    padding-left: 12px;
  }
</style>
</head>
<body>
  <section class="card card--front">
    <div class="brand">
      <div class="wordmark"><span class="wordmark__dot"></span>TARVIMOOR</div>
      <p class="brand__tagline">GMP &amp; JANITORIAL SERVICES</p>
    </div>
    <div class="divider"></div>
    <div class="contact">
      <p class="contact__name">Owen Hartley</p>
      <p class="contact__role">President</p>
      <p class="contact__address">2190 Ashcombe Lane<br>Brookvale, NY 11620</p>
      <ul class="contact__list">
        <li class="contact__item">
          <svg class="contact__icon" viewBox="0 0 14 14" aria-hidden="true"><path d="M1 4.5C1 2.5 3.5 1.5 7 1.5S13 2.5 13 4.5V5.5H10V4.3H4V5.5H1Z"/><path d="M3 6.5H11L12.5 12.5H1.5Z"/><circle cx="7" cy="9.5" r="1.6" fill="#fff"/></svg>
          (555) 2841-7730
        </li>
        <li class="contact__item">
          <svg class="contact__icon" viewBox="0 0 14 14" aria-hidden="true"><path d="M3.5 0.5H10.5V13.5H3.5ZM5 2V10.5H9V2Z"/><circle cx="7" cy="12" r="0.8" fill="#fff"/></svg>
          (555) 3904-1186
        </li>
        <li class="contact__item">
          <svg class="contact__icon" viewBox="0 0 14 14" aria-hidden="true"><path d="M3.5 1H10.5V5H3.5Z"/><path d="M1 5.8H13V10.5H11V8.5H3V10.5H1Z"/><path d="M3.8 9.3H10.2V13H3.8Z"/></svg>
          (555) 4417-2095
        </li>
        <li class="contact__item">
          <svg class="contact__icon" viewBox="0 0 14 14" aria-hidden="true"><path d="M1 3H13V4L7 8L1 4Z"/><path d="M1 5.3L7 9.3L13 5.3V11.5H1Z"/></svg>
          info@tarvimoor.com
        </li>
        <li class="contact__item">
          <svg class="contact__icon" viewBox="0 0 14 14" aria-hidden="true"><circle cx="7" cy="7" r="6.5"/><path d="M4 3.5C5.5 4 6 5.5 5 6.5S3 8 4 10M9 2.8C8.5 4.5 10 5 11 5.5M9.5 8.5C10.5 9.5 9.5 11 8.5 11.5" stroke="#fff" stroke-width="1.2" fill="none"/></svg>
          www.tarvimoor.com
        </li>
      </ul>
    </div>
  </section>

  <section class="card card--back">
    <div class="brand">
      <div class="brand__inner">
        <div class="wordmark"><span class="wordmark__dot"></span>TARVIMOOR</div>
        <p class="brand__tagline">GMP &amp; JANITORIAL SERVICES</p>
      </div>
    </div>
    <p class="website">www.tarvimoor.com</p>
  </section>
</body>
</html>
```